someone who can choose good colours and fonts and a style for an already layed out web page

HI

We need someone who can choose good colors and fonts and style for an already layed out web page.

please look at the first file.

The hard part of what needs to go where is already done,

1) we just need a type of character suitable for our business

2) colors probably in the green / yellow spectrum to suit our business

3) we need you to choose the style. For example you could choose round photos, or square buttons, video boxes with or without frames, that sort of stuff, just tweaking of what is there. plain arial is probably what we'd like but with text but with script or memorable headings. We would just like a design style that you think would be good gor our business model.

4) the twitter,facebook logo needs to be put in a new place

our project is an Italian style village in Italy called "Casale Delle Ginestre", in Abruzzo, Italy.
It is surrounded by vineyards, lake and olive trees.

The most important is that it looks expensive, the village is eco friendly so anything on those lines is great, Obviously Italian, so italian looking characters

our website is www.collinaserena.example but we are updating it. we like the style of the old site , but it is too out of date

you can create the layout using the files we've given below and boxes
Updates

hi we've just updated out brief to make it more simple, its actually not much work its just about design choices

Target Market(s)

all lovers of Italian things
eco frienly

Industry/Entity Type

Business

Font styles to use
Decorative
Script

Colors
fcf9ce
faee3f
fde18a
fece3e
cadf82
9bcb3b
acd036
fce7d2
ec2027

Requirements
Must have
• has to have the same layout or similar so as all the boxes and links are in there
twitter,facebook and other logos need to be present where you want them
Nice to have
• we have chosen some colors but you can choose others 3 or 4 are usual a good number with a light yellow background maybe....
Should not have
• no old style must look up to date

```html
<!DOCTYPE html>
<html lang="en">
<head>
<meta charset="utf-8">
<title>Casale Delle Ginestre – Italian Village in Abruzzo</title>
<link href="https://fonts.googleapis.com/css2?family=Great+Vibes&family=Dancing+Script:wght@400;700&family=Cinzel+Decorative:wght@400;700&family=Open+Sans:wght@400;600&family=Gelasio:wght@400;600&display=swap" rel="stylesheet">
<style>
:root{
  --cream:#fcf9d6;
  --page-top:#eef4cf;
  --page-bottom:#f6f8dc;
  --green-dark:#5a8512;
  --green:#7ba41f;
  --green-light:#9bcb3b;
  --menu:#86b12a;
  --menu-text:#f6f36a;
  --ink:#2f2f1f;
  --panel:#e9f2c8;
  --footer:#343431;
  --footer-text:#8fbf2c;
}
*{box-sizing:border-box;margin:0;padding:0}
html,body{width:1200px;height:2229px;overflow:hidden}
body{position:relative;background:linear-gradient(180deg,var(--page-top) 0%,#e4eebf 45%,var(--page-bottom) 100%);font-family:'Gelasio',Georgia,serif;color:var(--ink)}
.abs{position:absolute}

/* header */
.site-header{position:absolute;left:0;top:0;width:1200px;height:165px;background:var(--cream);border-bottom:2px solid #e2e8b8}
.brand-mark{left:22px;top:14px;width:132px;height:132px;border-radius:50%;background:var(--green)}
.brand-name{left:190px;top:38px;width:740px;text-align:center;white-space:nowrap;font-family:'Great Vibes',cursive;font-size:66px;color:#3f3f2c;line-height:1}
.contact{left:950px;font-family:'Open Sans',Arial,sans-serif;font-size:18px;color:#333;display:flex;align-items:center;gap:14px;white-space:nowrap}
.contact.phone{top:12px}.contact.address{top:58px;font-size:15px}
.flags{left:950px;top:124px;display:flex;gap:20px}
.flags span{width:28px;height:19px;display:block;border:1px solid #999}

/* nav */
.main-nav{left:318px;top:198px;display:flex;gap:30px;font-family:'Open Sans',Arial,sans-serif;font-size:20px;color:#222}
.main-nav .item{display:flex;align-items:center;gap:10px}
.main-nav .item.active{color:var(--green)}
.main-nav .caret{width:0;height:0;border-left:5px solid transparent;border-right:5px solid transparent;border-top:6px solid currentColor}
.nav-active-bar{left:318px;top:164px;width:118px;height:6px;background:var(--green)}
.dropdown{left:316px;top:230px;width:146px;background:var(--menu);box-shadow:2px 3px 6px rgba(0,0,0,.3);z-index:5}
.dropdown a{display:block;height:42px;line-height:42px;text-align:center;font-family:'Open Sans',Arial,sans-serif;font-size:15px;color:var(--menu-text);text-decoration:none;border-bottom:1px solid #a9cb55}
.dropdown a:last-child{border-bottom:none;height:50px;line-height:50px}

/* hero */
.site-map{left:27px;top:260px;width:558px;height:613px;background:linear-gradient(160deg,#f6f2dc 0%,#cfe39a 40%,#7fb34a 70%,#f1ecd2 100%);box-shadow:0 3px 8px rgba(0,0,0,.35)}
.slider{left:585px;top:260px;width:587px;height:613px;background:#3b4a2a;box-shadow:0 3px 8px rgba(0,0,0,.35)}
.slide-photo{left:0;top:0;width:587px;height:500px;background:linear-gradient(180deg,#8fb2c8 0%,#a98a6e 35%,#6d5a46 55%,#4f8a2c 75%,#3d7a23 100%)}
.slide-caption{left:168px;top:400px;width:415px;height:98px;background:rgba(220,225,210,.55);font-family:'Great Vibes',cursive;font-size:38px;color:#fff;text-align:center;line-height:98px;white-space:nowrap}
.thumbs{left:0;top:500px;width:587px;height:113px;background:rgba(40,50,30,.9)}
.thumb{top:506px;height:95px;border:2px solid #eee}
.thumb.current{border:5px solid #ccc}
.arrow{top:47px;width:0;height:0;border-top:9px solid transparent;border-bottom:9px solid transparent}

/* intro */
.intro{left:40px;top:916px;width:712px;font-family:'Dancing Script',cursive;font-size:21px;line-height:30px;color:#2b2b20}
.intro p{margin-bottom:30px}
.intro .lead{font-weight:700;font-size:31px;color:var(--green-dark)}
.intro .hl{color:var(--green)}
.section-title{font-family:'Cinzel Decorative',serif;font-style:italic;font-size:42px;color:var(--green);letter-spacing:2px}

/* seasons */
.season{top:1500px;width:134px;height:186px;border-radius:48% 52% 46% 50%/40% 40% 60% 60%}
.season-label{top:1684px;width:110px;height:30px;border-radius:15px;background:#4a4a44;color:#fff;font-family:'Gelasio',serif;font-size:15px;text-align:center;line-height:30px;box-shadow:0 3px 6px rgba(0,0,0,.4)}
.more-photos{left:280px;top:1728px;font-family:Arial,sans-serif;font-size:16px;color:#222}
.more-photos b{color:var(--green-dark);text-decoration:underline}

/* videos */
.video-title{font-family:'Gelasio',serif;font-size:17px;font-weight:600;color:#222}
.video-sub{font-family:'Gelasio',serif;font-size:17px;color:#8a8a7c}
.video{top:1856px;height:158px;background:linear-gradient(180deg,#7d9fc0 0%,#b7c3cc 40%,#4d5a3a 70%,#2d3322 100%);box-shadow:0 2px 5px rgba(0,0,0,.4)}
.play{left:50%;top:50%;width:36px;height:26px;margin:-13px 0 0 -18px;background:rgba(20,20,20,.8);border-radius:5px}
.play:after{content:"";position:absolute;left:14px;top:7px;border-left:10px solid #fff;border-top:6px solid transparent;border-bottom:6px solid transparent}

/* side panels */
.panel{left:788px;width:384px;background:var(--panel);box-shadow:3px 4px 6px rgba(0,0,0,.3)}
.panel-title{font-family:'Cinzel Decorative',serif;font-style:italic;font-size:38px;color:var(--green);text-align:center;padding-top:12px;letter-spacing:1px}
.label{font-family:'Gelasio',serif;font-size:16px;color:#222}
.field{height:33px;background:#fff;border:1px solid #999}
.btn{background:var(--green);color:#222;font-family:'Gelasio',serif;font-size:17px;text-align:center;line-height:33px;height:33px;box-shadow:1px 1px 3px rgba(0,0,0,.3)}
.post{font-family:'Gelasio',serif;font-size:19px;line-height:27px;color:#222}
.hint{color:#888;font-size:14px;padding-left:6px;line-height:31px;font-family:'Gelasio',serif}

/* footer */
.site-footer{left:0;top:2030px;width:1200px;height:199px;background:var(--footer)}
.foot-col{top:22px;font-family:'Gelasio',serif;color:var(--footer-text);font-size:14px;line-height:18px}
.foot-col h4{font-size:18px;font-weight:400;margin-bottom:2px}
.foot-col .cur{color:#fff;text-decoration:underline;font-style:italic;font-weight:600}
.social{left:985px;width:30px;height:30px;border-radius:50%;background:#8fbf2c}
.copyright{left:0;top:168px;width:1200px;text-align:center;font-family:'Gelasio',serif;font-size:12px;color:#ddd;line-height:14px}
</style>
</head>
<body>

<header class="site-header">
  <div class="abs brand-mark" aria-hidden="true"></div>
  <div class="abs brand-name">Casale Delle Ginestre</div>
  <div class="abs contact phone">
    <svg width="32" height="32" viewBox="0 0 32 32" aria-hidden="true"><rect x="3" y="10" width="26" height="19" rx="3" fill="none" stroke="#222" stroke-width="2"/><path d="M5 10 C5 3 27 3 27 10" fill="none" stroke="#222" stroke-width="2"/><circle cx="16" cy="20" r="5" fill="none" stroke="#222" stroke-width="2"/></svg>
    <span>0851234567</span>
  </div>
  <div class="abs contact address">
    <svg width="32" height="24" viewBox="0 0 32 24" aria-hidden="true"><rect x="1" y="2" width="30" height="20" fill="none" stroke="#222" stroke-width="2"/><path d="M1 2 L16 14 L31 2" fill="none" stroke="#222" stroke-width="2"/></svg>
    <span>Via dei Colli 12, Roccafiore</span>
  </div>
  <div class="abs flags" aria-label="Languages">
    <span style="background:linear-gradient(90deg,#2e8b3e 33%,#fff 33% 66%,#d33 66%)"></span>
    <span style="background:#2a3f8a"></span>
    <span style="background:linear-gradient(180deg,#111 33%,#d22 33% 66%,#f3c000 66%)"></span>
  </div>
</header>

<div class="abs nav-active-bar"></div>
<nav class="abs main-nav">
  <div class="item active">Description <span class="caret"></span></div>
  <div class="item">Which Reason <span class="caret"></span></div>
  <div class="item">PriceList <span class="caret"></span></div>
  <div class="item">Contact Us</div>
</nav>
<div class="abs dropdown">
  <a>Home</a><a>Styles</a><a>Alanno</a><a>Places NearBy</a><a>Borgo Shops</a><a>Phases</a>
</div>

<div class="abs site-map" role="img" aria-label="Illustrated site plan of the village showing phases A to D, gardens, lake, playground and parking"></div>

<div class="abs slider">
  <div class="abs slide-photo" role="img" aria-label="Photo of the villa courtyard with manicured lawn and cypress trees"></div>
  <div class="abs slide-caption">Refreshing Landscaped Gardens</div>
  <div class="abs thumbs">
    <div class="abs arrow" style="left:8px;border-right:11px solid #eee"></div>
    <div class="abs arrow" style="left:568px;border-left:11px solid #eee"></div>
  </div>
  <div class="abs thumb current" style="left:28px;width:100px;background:linear-gradient(#a8b9c4,#6a7a52)" role="img" aria-label="Villa thumbnail"></div>
  <div class="abs thumb" style="left:143px;width:86px;background:linear-gradient(#aab4c4,#e8ecf0)" role="img" aria-label="Snowy mountains thumbnail"></div>
  <div class="abs thumb" style="left:258px;width:82px;background:linear-gradient(#9bb0bd,#a67e5c)" role="img" aria-label="Stone house thumbnail"></div>
  <div class="abs thumb" style="left:370px;width:80px;background:linear-gradient(#3d6a2a,#8a6a3e)" role="img" aria-label="Woodland path thumbnail"></div>
  <div class="abs thumb" style="left:465px;width:83px;background:linear-gradient(#aebdd0,#8c9a86)" role="img" aria-label="Mountain view thumbnail"></div>
</div>

<section class="abs intro">
  <p><span class="lead">Casale Delle Ginestre</span> is built in traditional Italian architectural style and surrounded by olive groves, vineyards,<br>a beautiful lake surrounded by a park with wildlife. The panoramic view of the mountains is breathtaking and you can see for 30 miles on a clear day. <span class="hl">Red and white umbrellas</span>, <span class="hl">barbecues</span>, <span class="hl">swimming pools</span> and a <span class="hl">spa</span> will contribute to its unique atmosphere. there will also be a health farm, where you can treat yourself to a <span class="hl">luxurious massage</span>.</p>
  <p>Ten shops and ensure any of your other needs can be met. Casale Delle Ginestre is ensconced in the beauty of the Italian countryside, where the hot white sandy beaches of the <span class="hl">Adriatic coastline meet the cold snowy ski-slopes of the Appenine mountains</span>, with Rome only a short car ride away.</p>
  <p>Each property will be in the <span class="hl">OLD Abruzzo style</span>, with attractive brick and stone walls. There are one-, two- and three-bedroomed apartments and three- or four-bedroomed villas.</p>
</section>

<h2 class="abs section-title" style="left:40px;top:1422px">SEASONS</h2>
<div class="abs season" style="left:38px;background:linear-gradient(#7ea3c6,#3f7a2a 50%,#b33 85%)" role="img" aria-label="Spring meadow with poppies"></div>
<div class="abs season" style="left:206px;background:linear-gradient(#9bb7d6,#7b8a5c 50%,#8a6a3e)" role="img" aria-label="Autumn hills"></div>
<div class="abs season" style="left:387px;background:linear-gradient(#c8ccd0,#6f7670 55%,#4f5a48)" role="img" aria-label="Winter mountains in cloud"></div>
<div class="abs season" style="left:557px;background:linear-gradient(#b9cde0,#5f7a3a 50%,#3d5a22)" role="img" aria-label="Summer vineyard"></div>
<div class="abs season-label" style="left:50px">SPRING</div>
<div class="abs season-label" style="left:218px">AUTUMN</div>
<div class="abs season-label" style="left:399px">WINTER</div>
<div class="abs season-label" style="left:569px">SUMMER</div>
<div class="abs more-photos"><b>CLICK HERE</b> for More photos</div>

<h2 class="abs section-title" style="left:40px;top:1766px">VIDEOS</h2>
<div class="abs video-title" style="left:158px;top:1812px">Video 1</div>
<div class="abs video-sub" style="left:158px;top:1832px">Abruzzo Village Nov. 2010</div>
<div class="abs video" style="left:158px;width:192px" role="img" aria-label="Video still of the village with mountains"><span class="abs play"></span></div>
<div class="abs video-title" style="left:448px;top:1812px">Video 2</div>
<div class="abs video-sub" style="left:448px;top:1832px">Olive Harvest Nov. 2010</div>
<div class="abs video" style="left:448px;width:172px" role="img" aria-label="Video still of olive trees"><span class="abs play"></span></div>

<aside class="abs panel" style="top:918px;height:277px">
  <div class="panel-title">NEWSLETTER</div>
  <div class="abs" style="left:0;top:72px;width:384px;text-align:center;font-size:20px">Sign Up for Our NewsLetter</div>
  <div class="abs label" style="left:20px;top:128px">Name</div>
  <div class="abs field" style="left:88px;top:122px;width:275px"></div>
  <div class="abs label" style="left:20px;top:184px">Email</div>
  <div class="abs field" style="left:88px;top:179px;width:275px"></div>
  <div class="abs btn" style="left:240px;top:237px;width:122px">Submit</div>
</aside>

<aside class="abs panel" style="top:1228px;height:372px">
  <div class="panel-title">BLOGS</div>
  <div class="abs post" style="left:30px;top:84px;width:340px">Post 1 : Why should we retire in Italy? .... (2 comments)</div>
  <div class="abs post" style="left:30px;top:164px;width:340px">Post 2: Information for US Citizens .... (5 comments)</div>
  <div class="abs post" style="left:30px;top:240px;width:340px">Post 3: Lorem ipsum dolor sit amet. dolor sit .... (0 comments)</div>
  <div class="abs" style="left:30px;top:304px;font-size:16px;color:var(--green-dark)">Read More &gt;&gt;</div>
  <div class="abs btn" style="left:200px;top:322px;width:175px;font-size:16px">Browse Older Posts</div>
</aside>

<aside class="abs panel" style="top:1630px;height:370px">
  <div class="panel-title">BOOK TRIP</div>
  <div class="abs label" style="left:22px;top:82px">Name</div>
  <div class="abs field" style="left:157px;top:75px;width:215px"></div>
  <div class="abs label" style="left:22px;top:122px">Check-In Date</div>
  <div class="abs field" style="left:157px;top:115px;width:215px"><span class="hint">mm/dd/yyyy</span></div>
  <div class="abs label" style="left:22px;top:162px">Check-Out Date</div>
  <div class="abs field" style="left:157px;top:155px;width:215px"><span class="hint">mm/dd/yyyy</span></div>
  <div class="abs label" style="left:22px;top:202px">No. Of Persons</div>
  <div class="abs label" style="left:80px;top:226px;font-size:14px">Adult</div>
  <div class="abs field" style="left:157px;top:222px;width:55px;height:28px"><span class="hint" style="line-height:26px">1</span></div>
  <div class="abs label" style="left:245px;top:226px;font-size:14px">Children</div>
  <div class="abs field" style="left:317px;top:222px;width:57px;height:28px"><span class="hint" style="line-height:26px">0</span></div>
  <div class="abs label" style="left:30px;top:276px">Email</div>
  <div class="abs field" style="left:157px;top:270px;width:215px"></div>
  <div class="abs btn" style="left:247px;top:328px;width:123px;font-size:16px">BOOK NOW</div>
</aside>

<footer class="abs site-footer">
  <div class="abs foot-col" style="left:285px"><h4>Description</h4>- <span class="cur">Home</span><br>- Styles<br>- Alanno<br>- Places NearBy<br>- Borgo Shops<br>- Phases</div>
  <div class="abs foot-col" style="left:465px"><h4>Which Reason?</h4>- Reasons<br>- Motives</div>
  <div class="abs foot-col" style="left:645px"><h4>Prices</h4>- Buying Procedure<br>- Price List<br>- Mortgage</div>
  <div class="abs foot-col" style="left:825px"><h4>Contact Us</h4></div>
  <div class="abs social" style="top:36px" role="img" aria-label="Social link"></div>
  <div class="abs social" style="top:85px" role="img" aria-label="Social link"></div>
  <div class="abs social" style="top:132px" role="img" aria-label="Social link"></div>
  <div class="abs copyright">(c) 2013 Casale Delle Ginestre - CasaColline Viaggi S.r.l.<br>More properties for sale in Abruzzo, CasaColline Italia</div>
</footer>

</body>
</html>
```